Need to create a website for a luxury custom home builder in Phoenix USA. Looking forward for some creative designs including a full page video intro on homepage and should show up pretty luxurious.

```html
<!DOCTYPE html>
<html lang="en">
<head>
<meta charset="utf-8">
<title>Stonecrest Homes — Luxury Custom Home Builder, Phoenix</title>
<link href="https://fonts.googleapis.com/css2?family=Poppins:wght@300;400;500;600;700&display=swap" rel="stylesheet">
<style>
:root{
  --blue:#1e8fd8;
  --teal:#1aa893;
  --ink:#1d1d1f;
  --body:#3c3c40;
  --muted:#6b6b72;
  --tint:#eef5fb;
  --white:#ffffff;
  --star:#f5a623;
}
*{box-sizing:border-box;margin:0;padding:0}
html,body{width:1200px;height:4277px;overflow:hidden}
body{font-family:'Poppins',sans-serif;color:var(--ink);background:var(--white);position:relative}
.abs{position:absolute}
section,header,footer{position:absolute;left:0;width:1200px;overflow:hidden}

/* photo areas: soft layered tones */
.photo-fill{position:relative;overflow:hidden}
.photo-fill::before{content:"";position:absolute;inset:0;background:radial-gradient(ellipse at 50% 40%,rgba(255,255,255,.18),transparent 60%),linear-gradient(180deg,transparent 60%,rgba(0,0,0,.18));pointer-events:none}

/* hero */
.hero{top:0;height:674px;
  background:
    radial-gradient(ellipse 420px 300px at 1060px 360px,rgba(74,104,44,.95),transparent 70%),
    radial-gradient(ellipse 260px 380px at 60px 420px,rgba(48,68,38,.9),transparent 70%),
    radial-gradient(ellipse 520px 260px at 560px 300px,rgba(236,238,240,.85),transparent 70%),
    radial-gradient(ellipse 700px 200px at 600px 640px,rgba(96,100,98,.9),transparent 70%),
    linear-gradient(180deg,#2c3e5c 0%,#51627c 28%,#8c97a3 52%,#5d6462 74%,#3a403c 100%)}
.hero-shade{position:absolute;inset:0;background:linear-gradient(90deg,rgba(12,20,34,.55),rgba(12,20,34,.18) 65%,rgba(12,20,12,.25)),linear-gradient(180deg,rgba(10,16,28,.45),transparent 22%,transparent 80%,rgba(10,10,10,.35))}
.brand{display:flex;align-items:center;gap:10px;color:var(--white);font-weight:600;font-size:24px;letter-spacing:.5px}
.brand .dot{width:30px;height:30px;border-radius:50%;background:var(--white)}
.hero .brand{left:161px;top:22px}
.nav{left:496px;top:31px;display:flex;gap:28px;font-size:13px;color:var(--white)}
.nav a{color:inherit;text-decoration:none}
.nav-sep{left:1000px;top:28px;width:1px;height:24px;background:rgba(255,255,255,.4)}
.search{left:1023px;top:33px}
.hero h1{left:161px;top:250px;font-size:52px;font-weight:600;color:var(--white);letter-spacing:1px;text-shadow:0 2px 12px rgba(0,0,0,.25)}
.hero .line2{left:161px;top:326px;font-size:43px;font-weight:500;color:var(--white);letter-spacing:2px;text-shadow:0 2px 12px rgba(0,0,0,.25)}
.hero .line3{left:161px;top:392px;font-size:25px;font-weight:400;color:var(--white);letter-spacing:.75em}
.hero-arrows{left:161px;top:622px}
.scroll{left:540px;top:624px;width:120px;text-align:center;font-size:9px;letter-spacing:1px;color:var(--white)}
.social-rail{left:1158px;top:374px;width:16px;text-align:center}
.social-rail .bar{width:1px;height:50px;background:rgba(255,255,255,.7);margin:0 auto 58px}
.social-rail span{display:block;width:9px;height:9px;border:1.5px solid var(--white);border-radius:50%;margin:0 auto 33px}

/* about */
.about{top:674px;height:654px;background:var(--white)}
.about-photo1{left:161px;top:75px;width:342px;height:455px;
  background:
    radial-gradient(ellipse 120px 40px at 170px 60px,rgba(200,160,100,.6),transparent 70%),
    radial-gradient(ellipse 140px 60px at 110px 320px,rgba(236,232,226,.95),transparent 70%),
    radial-gradient(ellipse 90px 70px at 40px 380px,rgba(40,40,40,.85),transparent 70%),
    linear-gradient(90deg,rgba(230,228,222,.6),transparent 20%,transparent 80%,rgba(210,205,196,.6)),
    linear-gradient(180deg,#ece9e3 0%,#d9cfc2 25%,#9f8468 48%,#c7bcae 68%,#6f6a64 100%)}
.about-photo2{left:380px;top:353px;width:173px;height:221px;border:6px solid var(--white);
  background:
    radial-gradient(ellipse 60px 30px at 80px 170px,rgba(176,124,64,.95),transparent 75%),
    radial-gradient(ellipse 70px 110px at 80px 90px,rgba(230,222,210,1),transparent 75%),
    linear-gradient(180deg,#f4efe8,#e2d6c4 60%,#c9b498)}
.about-title{left:611px;top:118px;font-size:36px;line-height:43px;font-weight:300;color:var(--ink)}
.about-title b{font-weight:600}
.about-text{left:611px;top:208px;width:430px;font-size:12.5px;line-height:24px;color:var(--body)}
.about-text p+p{margin-top:16px}
.btn{display:inline-flex;align-items:center;justify-content:center;border:1.5px solid var(--blue);color:var(--blue);font-size:12.5px;font-weight:500;background:var(--white)}
.about .btn{left:611px;top:443px;width:166px;height:38px}

/* custom built */
.custom{top:1328px;height:523px;background:var(--tint)}
.section-title{left:0;width:1200px;text-align:center;font-size:36px;font-weight:300;color:var(--ink);letter-spacing:.5px}
.section-title b{font-weight:600}
.custom .section-title{top:66px}
.custom .lead{left:340px;top:114px;width:520px;text-align:center;font-size:12.5px;line-height:24px;color:var(--body)}
.card{width:271px}
.card .photo{height:201px}
.card h3{margin-top:18px;text-align:center;font-size:13.5px;font-weight:500}
.card p{margin-top:4px;text-align:center;font-size:12px;color:var(--muted)}
.card.active h3{text-decoration:underline}
.round-arrow{width:36px;height:36px;border-radius:50%;border:1.5px solid #c8d2dc;display:flex;align-items:center;justify-content:center}

/* projects */
.projects{top:1851px;height:750px;background:var(--white)}
.projects .section-title{top:66px}
.tile{position:absolute}
.projects .btn{left:518px;top:637px;width:164px;height:39px}

/* testimonials */
.reviews{top:2601px;height:603px;background:var(--tint)}
.reviews .section-title{top:66px}
.review{top:136px;width:278px;height:352px;background:var(--white);box-shadow:0 2px 10px rgba(30,60,90,.06);text-align:center}
.avatar{width:66px;height:66px;border-radius:50%;margin:33px auto 0}
.stars{margin-top:12px;color:var(--star);font-size:16px;letter-spacing:2px}
.review p{margin:6px auto 0;width:212px;font-size:12px;line-height:22.5px;color:var(--body)}
.review .who{margin-top:12px;font-size:12.5px;color:var(--ink)}
.dots{left:0;width:1200px;top:517px;display:flex;justify-content:center;gap:10px;align-items:center}
.dots i{width:7px;height:7px;border-radius:50%;background:#b9d7ee}
.dots i.on{width:10px;height:10px;border:2px solid var(--blue);background:var(--white)}

/* news */
.news{top:3204px;height:634px;background:var(--white)}
.news .section-title{top:66px}
.post{position:absolute;overflow:hidden}
.post .cap{position:absolute;left:32px;bottom:28px;color:var(--white);font-size:13px;font-weight:500;line-height:23px;z-index:1}
.post .date{display:flex;align-items:center;gap:8px;font-size:11px;font-weight:400}
.post::after{content:"";position:absolute;inset:0;background:linear-gradient(180deg,transparent 45%,rgba(0,0,0,.6))}

/* footer */
.footer{top:3838px;height:439px;
  background:
    radial-gradient(ellipse 260px 120px at 600px 120px,rgba(150,120,80,.35),transparent 70%),
    radial-gradient(ellipse 200px 260px at 80px 360px,rgba(40,60,40,.8),transparent 70%),
    radial-gradient(ellipse 220px 260px at 1120px 340px,rgba(50,66,48,.7),transparent 70%),
    linear-gradient(180deg,#46505c 0%,#373d44 45%,#2c3034 100%)}
.footer-shade{position:absolute;inset:0;background:rgba(12,16,22,.5)}
.footer .brand{left:0;width:1200px;justify-content:center;top:94px;color:var(--teal);font-size:26px}
.footer .brand .dot{background:var(--teal)}
.footer-nav{left:0;width:1200px;top:176px;display:flex;justify-content:center;gap:34px;font-size:12.5px;color:var(--white)}
.footer-nav .on{color:var(--teal)}
.contact{display:flex;align-items:center;gap:16px;color:var(--white);font-size:12.5px;line-height:22px}
.contact .ico{width:60px;height:60px;border-radius:50%;display:flex;align-items:center;justify-content:center;flex:none}
.copy{left:0;width:1200px;top:346px;text-align:center;font-size:12px;color:rgba(255,255,255,.8)}
.foot-social{left:0;width:1200px;top:384px;display:flex;justify-content:center;gap:14px}
.foot-social span{width:30px;height:30px;border-radius:50%;border:1px solid rgba(255,255,255,.35)}
.foot-social span.on{background:var(--blue);border-color:var(--blue)}
</style>
</head>
<body>

<header class="hero" role="img" aria-label="Full-width video intro: modern white luxury villa with glass walls and palm trees at dusk">
  <div class="hero-shade"></div>
  <div class="abs brand"><span class="dot"></span>STONECREST HOMES</div>
  <nav class="abs nav"><a href="#">Home</a><a href="#">About Us</a><a href="#">Services</a><a href="#">Gallery</a><a href="#">Reviews</a><a href="#">Contact Us</a></nav>
  <div class="abs nav-sep"></div>
  <svg class="abs search" width="16" height="16" viewBox="0 0 16 16" fill="none" stroke="#fff" stroke-width="1.8"><circle cx="7" cy="7" r="5"/><path d="M11 11l3.5 3.5"/></svg>
  <h1 class="abs">Explore visions</h1>
  <div class="abs line2">without boundries, we build</div>
  <div class="abs line3">the Future imagined</div>
  <svg class="abs hero-arrows" width="120" height="16" viewBox="0 0 120 16" fill="none" stroke="#fff" stroke-width="1.4"><path d="M44 8H2M8 3L2 8l6 5"/><path d="M74 8h42M110 3l6 5-6 5"/></svg>
  <div class="abs scroll">SCROLL DOWN<br><svg width="12" height="8" viewBox="0 0 12 8" fill="none" stroke="#fff" stroke-width="1.2"><path d="M1 2l5 4 5-4"/></svg></div>
  <div class="abs social-rail"><div class="bar"></div><span></span><span></span><span></span><span></span></div>
</header>

<section class="about">
  <div class="abs about-photo1" role="img" aria-label="Warm modern living room with round pendant light and curved sofa"></div>
  <div class="abs about-photo2" role="img" aria-label="Arched alcove with a tan lounge chair"></div>
  <h2 class="abs about-title">ABOUT<br><b>STONECREST HOMES</b></h2>
  <div class="abs about-text">
    <p>Lorem Ipsum is simply dummy text of the printing and typesetting industry. Lorem Ipsum has been the industry's standard dummy text ever since the 1500s, when an unknown printer took a galley of type and scrambled it to make a type specimen book. It has survived not only five centuries, but also the leap into electronic typesetting, remaining essentially unchanged.</p>
    <p>It was popularised in the 1960s with the release of Letraset sheets containing Lorem Ipsum passages, and more recently.</p>
  </div>
  <a class="abs btn">Contact Us Today!</a>
</section>

<section class="custom">
  <h2 class="abs section-title"><b>CUSTOM BUILT</b> HOMES</h2>
  <p class="abs lead">Lorem Ipsum is simply dummy text of the printing and typesetting industry. Lorem Ipsum has been the industry's standard dummy text</p>
  <div class="abs round-arrow" style="left:92px;top:272px"><svg width="12" height="10" viewBox="0 0 12 10" fill="none" stroke="#9aa8b5" stroke-width="1.3"><path d="M11 5H1M5 1L1 5l4 4"/></svg></div>
  <div class="abs round-arrow" style="left:1071px;top:272px"><svg width="12" height="10" viewBox="0 0 12 10" fill="none" stroke="#9aa8b5" stroke-width="1.3"><path d="M1 5h10M7 1l4 4-4 4"/></svg></div>
  <div class="abs card" style="left:161px;top:191px">
    <div class="photo photo-fill" role="img" aria-label="White modern house with infinity pool" style="background:radial-gradient(ellipse 150px 45px at 140px 85px,rgba(248,248,246,1),transparent 75%),radial-gradient(ellipse 60px 50px at 250px 120px,rgba(90,120,70,.8),transparent 75%),linear-gradient(180deg,#3f74b8 0%,#8fb2d8 30%,#dfe3e4 45%,#a9adaa 58%,#2a8ab8 72%,#1d6f98 100%)"></div>
    <h3>Custom Home Title</h3><p>It is a long established fact that...</p>
  </div>
  <div class="abs card active" style="left:465px;top:191px">
    <div class="photo" role="img" aria-label="Modern home with blue hover overlay" style="background:radial-gradient(ellipse 140px 70px at 135px 80px,rgba(90,180,240,.5),transparent 75%),linear-gradient(180deg,#2a9ae0,#1e8fd8 60%,#1b86cc);display:flex;align-items:center;justify-content:center">
      <svg width="34" height="34" viewBox="0 0 34 34" fill="none" stroke="#fff" stroke-width="1.4"><circle cx="17" cy="17" r="15"/><path d="M13 21l8-8M14 13h7v7"/></svg>
    </div>
    <h3>Custom Home Title</h3><p>It is a long established fact that...</p>
  </div>
  <div class="abs card" style="left:769px;top:191px">
    <div class="photo photo-fill" role="img" aria-label="Modern house lit at night with turquoise pool" style="background:radial-gradient(ellipse 170px 40px at 170px 70px,rgba(200,225,240,.8),transparent 75%),radial-gradient(ellipse 160px 35px at 130px 165px,rgba(40,220,240,.9),transparent 75%),linear-gradient(180deg,#050608 0%,#151b24 30%,#5a6d80 48%,#1a2a38 62%,#0f8fb0 80%,#0b4d66 100%)"></div>
    <h3>Custom Home Title</h3><p>It is a long established fact that...</p>
  </div>
</section>

<section class="projects">
  <h2 class="abs section-title">OUR <b>PROJECTS</b></h2>
  <div class="tile photo-fill" role="img" aria-label="White colonial house with brick chimney and paved courtyard" style="left:161px;top:139px;width:286px;height:460px;background:radial-gradient(ellipse 150px 110px at 170px 230px,rgba(240,240,236,.95),transparent 75%),radial-gradient(ellipse 40px 90px at 175px 110px,rgba(140,60,40,.8),transparent 75%),radial-gradient(ellipse 180px 70px at 140px 410px,rgba(150,110,90,.9),transparent 75%),linear-gradient(180deg,#3e78c0 0%,#7fa5d2 22%,#c9d3d8 42%,#7a9560 68%,#4e6c3a 80%,#8a6e5c 100%)"></div>
  <div class="tile photo-fill" role="img" aria-label="White modern two-storey house among palm trees" style="left:458px;top:139px;width:344px;height:224px;background:radial-gradient(ellipse 130px 80px at 150px 100px,rgba(246,244,240,1),transparent 75%),radial-gradient(ellipse 70px 110px at 310px 100px,rgba(80,120,60,.85),transparent 75%),linear-gradient(180deg,#d6e0e8 0%,#ecebe6 50%,#b8b7ae 72%,#4e7c3e 100%)"></div>
  <div class="tile photo-fill" role="img" aria-label="Grey contemporary house with stone base" style="left:813px;top:139px;width:226px;height:224px;background:radial-gradient(ellipse 90px 70px at 110px 100px,rgba(110,125,135,.9),transparent 75%),radial-gradient(ellipse 110px 30px at 110px 195px,rgba(150,140,125,.9),transparent 75%),linear-gradient(180deg,#cfe0f0 0%,#a6b2bb 35%,#6f7a82 65%,#9a968c 100%)"></div>
  <div class="tile photo-fill" role="img" aria-label="Grey craftsman house with red front garden" style="left:458px;top:375px;width:224px;height:224px;background:radial-gradient(ellipse 80px 70px at 110px 110px,rgba(120,125,128,.9),transparent 75%),radial-gradient(ellipse 110px 30px at 110px 205px,rgba(140,70,50,.85),transparent 75%),linear-gradient(180deg,#e9edf0 0%,#a7acaf 35%,#7d8286 65%,#6c5c4a 100%)"></div>
  <div class="tile photo-fill" role="img" aria-label="Modern villa lit at dusk under deep blue sky" style="left:694px;top:375px;width:345px;height:224px;background:radial-gradient(ellipse 150px 50px at 170px 140px,rgba(255,230,180,.85),transparent 75%),radial-gradient(ellipse 160px 50px at 170px 80px,rgba(230,226,215,.9),transparent 75%),linear-gradient(180deg,#17357e 0%,#2d51a0 35%,#b7b3a6 55%,#6e6a62 80%,#3b3a36 100%)"></div>
  <a class="abs btn">View Full Portfolio</a>
</section>

<section class="reviews">
  <h2 class="abs section-title">WHAT PEOPLE <b>ARE SAYING</b></h2>
  <div class="abs review" style="left:161px">
    <div class="avatar" role="img" aria-label="Client portrait" style="background:radial-gradient(circle at 50% 45%,#b08a70,#5a4a40 70%),#9bb7c9"></div>
    <div class="stars">★★★★★</div>
    <p>Lorem There are many variations of passages of Lorem Ipsum available, but the majority have suffered alteration in some form, by injected humour, or randomised words which don't look even slightly believable. If you are going to use.</p>
    <div class="who">- Maren Holt</div>
  </div>
  <div class="abs review" style="left:461px">
    <div class="avatar" role="img" aria-label="Client portrait" style="background:radial-gradient(circle at 50% 50%,#555,#111 75%)"></div>
    <div class="stars">★★★★★</div>
    <p>Lorem There are many variations of passages of Lorem Ipsum available, but the majority have suffered alteration in some form, by injected humour, or randomised words which don't look even slightly believable. If you are going to use.</p>
    <div class="who">- Dario Kent</div>
  </div>
  <div class="abs review" style="left:761px">
    <div class="avatar" role="img" aria-label="Client portrait" style="background:radial-gradient(circle at 50% 55%,#8a7464,#5a4a40 60%,#f2c58a 100%)"></div>
    <div class="stars">★★★★★</div>
    <p>Lorem There are many variations of passages of Lorem Ipsum available, but the majority have suffered alteration in some form, by injected humour, or randomised words which don't look even slightly believable. If you are going to use.</p>
    <div class="who">- Tomas Reyes</div>
  </div>
  <div class="abs dots"><i></i><i class="on"></i><i></i><i></i></div>
</section>

<section class="news">
  <h2 class="abs section-title">LATEST <b>NEWS</b></h2>
  <article class="post" role="img" aria-label="Large grey family house with white trim at dusk" style="left:161px;top:133px;width:427px;height:426px;background:radial-gradient(ellipse 190px 120px at 210px 170px,rgba(140,140,138,.9),transparent 75%),radial-gradient(ellipse 60px 50px at 200px 280px,rgba(255,210,150,.5),transparent 75%),linear-gradient(180deg,#e4e8ec 0%,#b9bdc0 25%,#7d8184 50%,#4f5450 72%,#2c3828 100%)">
    <div class="cap"><div class="date"><svg width="14" height="14" viewBox="0 0 14 14" fill="none" stroke="#1aa893" stroke-width="1.3"><rect x="1" y="2.5" width="12" height="10.5" rx="1"/><path d="M1 6h12M4 1v3M10 1v3"/></svg>10 Oct 2023</div>Lorem Ipsum is simply dummy text of the printing<br>and typesetting industry</div>
  </article>
  <article class="post" role="img" aria-label="Modern wooden house among trees at twilight" style="left:611px;top:133px;width:428px;height:200px;background:radial-gradient(ellipse 90px 40px at 200px 120px,rgba(255,190,110,.7),transparent 75%),radial-gradient(ellipse 140px 60px at 330px 110px,rgba(120,80,50,.9),transparent 75%),linear-gradient(180deg,#56677a 0%,#3a4440 45%,#2e3028 70%,#4a3a2a 100%)">
    <div class="cap"><div class="date"><svg width="14" height="14" viewBox="0 0 14 14" fill="none" stroke="#1aa893" stroke-width="1.3"><rect x="1" y="2.5" width="12" height="10.5" rx="1"/><path d="M1 6h12M4 1v3M10 1v3"/></svg>10 Oct 2023</div>It is a long established fact that a reader</div>
  </article>
  <article class="post" role="img" aria-label="Glass pool house at sunset" style="left:611px;top:357px;width:428px;height:202px;background:radial-gradient(ellipse 150px 50px at 260px 90px,rgba(255,200,140,.7),transparent 75%),radial-gradient(ellipse 200px 30px at 220px 170px,rgba(60,150,190,.9),transparent 75%),linear-gradient(180deg,#3f4e70 0%,#8a7a86 25%,#c99778 42%,#6e5040 65%,#2f6f8f 100%)">
    <div class="cap"><div class="date"><svg width="14" height="14" viewBox="0 0 14 14" fill="none" stroke="#1aa893" stroke-width="1.3"><rect x="1" y="2.5" width="12" height="10.5" rx="1"/><path d="M1 6h12M4 1v3M10 1v3"/></svg>10 Oct 2023</div>Contrary to popular belief, Lorem Ipsum is not simply</div>
  </article>
</section>

<footer class="footer" role="img" aria-label="Dark photo of a modern house at night behind the footer">
  <div class="footer-shade"></div>
  <div class="abs brand"><span class="dot"></span>STONECREST HOMES</div>
  <nav class="abs footer-nav"><span class="on">Home</span><span>About</span><span>Our Projects</span><span>Latest News</span><span>Contact Us</span></nav>
  <div class="abs contact" style="left:161px;top:245px">
    <span class="ico" style="background:var(--blue)"><svg width="26" height="26" viewBox="0 0 26 26" fill="none" stroke="#fff" stroke-width="1.5"><path d="M13 23s-7-7-7-12a7 7 0 0114 0c0 5-7 12-7 12z"/><circle cx="13" cy="11" r="2.5"/></svg></span>
    <span>123, Lorem There are many variations<br>of passages of, Phoenix USA.</span>
  </div>
  <div class="abs contact" style="left:533px;top:245px">
    <span class="ico" style="background:var(--teal)"><svg width="26" height="26" viewBox="0 0 26 26" fill="none" stroke="#fff" stroke-width="1.5"><rect x="4" y="6" width="18" height="14" rx="1.5"/><path d="M4 7l9 7 9-7"/></svg></span>
    <span>info@stonecresthomes.com</span>
  </div>
  <div class="abs contact" style="left:845px;top:245px;font-size:16px">
    <span class="ico" style="background:var(--blue)"><svg width="26" height="26" viewBox="0 0 26 26" fill="none" stroke="#fff" stroke-width="1.5"><path d="M7 4l3 4-2 2c1 3 3 5 6 6l2-2 4 3-2 4C11 20 6 15 4 7z"/></svg></span>
    <span>(123) 456-7890</span>
  </div>
  <div class="abs copy">© 2023 Stonecrest Homes. All Rights Reserved.</div>
  <div class="abs foot-social"><span></span><span class="on"></span><span></span></div>
</footer>

</body>
</html>
```